Laptop Accessories Packing Design

We are looking for a new package design of a laptop accesories (batteries, charges, hard drives etc.). We want to refresh our brand Velmora GridWorks. At VelmoraGrid, we create high-end laptop accessories that ensure reliability, performance, and longevity for users worldwide. Our mission is to deliver innovative and durable solutions that allow users to work, create, and grow without limits.
General Packaging Concept
Minimalist and elegant look, yet with elements that catch the eye (Velmora products will mainly be offered on auction portals such as Trivana, Zubo, Kestrix, so it would be good if the packaging attracted attention and stood out from the competitors).
Should I put a photo, sketch or product icon on the box? We'll leave that to your imagination.
We ask for a general design of the packaging. After the competition, together with the winner, we will add the rest of the information to the back and sides of the box.
In the attachments there is our Logo (you can use other colors) and sample packaging of competitors
Target Market(s)
E-commerse
Industry/Entity Type
individual end customer
Look and feel
Each slider illustrates characteristics of the customer's brand and the style your logo design should communicate.

```html
<!DOCTYPE html>
<html lang="en">
<head>
<meta charset="utf-8">
<title>Velmora GridWorks – Laptop Battery Box</title>
<link rel="stylesheet" href="https://fonts.googleapis.com/css2?family=Saira+Semi+Condensed:wght@400;600;800&display=swap">
<style>
  :root {
    --bg: #e4e4e4;
    --yellow: #eee53a;
    --yellow-light: #f3ec63;
    --ink: #262424;
  }
  html, body {
    margin: 0;
    width: 1200px;
    height: 806px;
    overflow: hidden;
    background: var(--bg);
    font-family: "Saira Semi Condensed", "Arial Narrow", sans-serif;
  }
  .package {
    position: absolute;
    left: 100px;
    top: 183px;
    width: 1000px;
    height: 440px;
    display: flex;
  }
  .side-panel {
    position: relative;
    width: 100px;
    height: 100%;
    background: var(--ink);
    overflow: hidden;
  }
  .side-panel svg { position: absolute; left: 0; top: 0; }
  .side-brand {
    position: absolute;
    left: 50%;
    top: 290px;
    transform: translate(-50%, -50%) rotate(90deg);
    white-space: nowrap;
    color: var(--yellow);
    font-weight: 800;
    font-size: 24px;
    line-height: 1;
  }
  .front-panel {
    position: relative;
    flex: 1;
    background: linear-gradient(100deg, var(--yellow-light), var(--yellow) 60%);
    overflow: hidden;
  }
  .accent-band {
    position: absolute;
    right: 0;
    top: 0;
    width: 150px;
    height: 100%;
    background: var(--ink);
  }
  .brand-name {
    position: absolute;
    left: 66px;
    top: 44px;
    margin: 0;
    color: var(--ink);
    font-weight: 800;
    font-size: 56px;
    line-height: 1;
    white-space: nowrap;
  }
  .headline {
    position: absolute;
    left: 66px;
    top: 210px;
    margin: 0;
    color: var(--ink);
    font-size: 34px;
    line-height: 1;
    font-weight: 400;
    white-space: nowrap;
  }
  .headline strong { font-weight: 800; }
  .features {
    position: absolute;
    left: 66px;
    top: 304px;
    display: flex;
    gap: 14px;
    list-style: none;
    margin: 0;
    padding: 0;
  }
  .feature {
    width: 88px;
    height: 104px;
    box-sizing: border-box;
    border: 2px solid var(--ink);
    border-radius: 16px;
    display: flex;
    flex-direction: column;
    align-items: center;
    justify-content: flex-end;
    padding-bottom: 10px;
    color: var(--ink);
    text-align: center;
  }
  .feature svg { margin-bottom: 4px; }
  .feature-label {
    font-weight: 800;
    font-size: 12px;
    line-height: 1.05;
    text-transform: uppercase;
  }
  .feature-label.big { font-size: 16px; }
</style>
</head>
<body>
  <main class="package">
    <section class="side-panel">
      <svg width="100" height="140" viewBox="0 0 100 140" aria-hidden="true">
        <line x1="0" y1="110" x2="70" y2="0" stroke="var(--yellow)" stroke-width="3"/>
        <line x1="0" y1="130" x2="83" y2="0" stroke="var(--yellow)" stroke-width="2"/>
      </svg>
      <div class="side-brand">Velmora GridWorks</div>
    </section>

    <section class="front-panel">
      <div class="accent-band"></div>
      <h1 class="brand-name">Velmora GridWorks</h1>

      <p class="headline"><strong>Hi- Performance</strong> Laptop Batterie</p>

      <ul class="features">
        <li class="feature">
          <svg width="44" height="44" viewBox="0 0 44 44" aria-hidden="true">
            <text x="22" y="38" text-anchor="middle" font-family="Saira Semi Condensed, sans-serif" font-weight="800" font-size="44" fill="var(--ink)">A</text>
          </svg>
          <span class="feature-label">Grad Cells</span>
        </li>
        <li class="feature">
          <svg width="50" height="36" viewBox="0 0 50 36" aria-hidden="true">
            <rect x="3" y="6" width="38" height="24" rx="2" fill="none" stroke="var(--ink)" stroke-width="4"/>
            <rect x="42" y="13" width="5" height="10" fill="var(--ink)"/>
            <path d="M26 2 L15 20 H23 L19 34 L32 14 H24 Z" fill="var(--ink)"/>
          </svg>
          <span class="feature-label">Higher<br>Capacity</span>
        </li>
        <li class="feature">
          <svg width="36" height="38" viewBox="0 0 36 38" aria-hidden="true">
            <circle cx="18" cy="15" r="12" fill="none" stroke="var(--ink)" stroke-width="3"/>
            <path d="M12 15 L16 19 L24 11" fill="none" stroke="var(--ink)" stroke-width="3"/>
            <path d="M11 25 L8 36 L13 33 L16 37 L17 28" fill="var(--ink)"/>
            <path d="M25 25 L28 36 L23 33 L20 37 L19 28" fill="var(--ink)"/>
          </svg>
          <span class="feature-label big">1 Year</span>
          <span class="feature-label">Warranty</span>
        </li>
      </ul>
    </section>
  </main>
</body>
</html>
```